Harborline Safety Courses

I'm currently in the process of setting up a First Aid and Lifeguard Training website. The project has already began through a web designer but he is unable to meet the deadline.
There's is already a landing page
http://www.harborlinesafetycourses.example.au/
In addition he also started to create the website
https://mockups.example.net/view/9c41d7e0-5b2a-4e8f-a613-d02e7bb18c39-2218/?fullscreen
The home page ideally needs to have a different visual and user journey from the quick landing page created
- The Logo in the top left hand corner looks a bit out of whack, maybe it needs to be bigger ??
-The tabs along the top need to be 'designed' and spaced out equally: home, about, courses, contact, gallery. Can we please remove Accredited First Aid and Lifeguard.
-the blue bar with the tag line needs to be redesigned - that was ok for a landing page but not quite right for actual website, it looks clunky
-all the course info needs to be placed under the courses tab not on the home page. I would like a roll down bar ( Check out Tidewater Rescue Aid website on their First Aid Course) so the client can book a date and proceed to the checkout basket. I will supply those soon; this will only apply to the Provide First Aid and Provide Cardiopulmonary Resuscitation Courses.
- The rest of the courses can have an enquire option
-the about paragraphs need to go directly under banner
-then a rolling slider with upcoming courses - with each course, rolling to give the home page some pop
- followed by pictures/ images of recent courses linked to gallery page updates or social feed
-remove newsletter
In addition to this I also have a logo designed via sketch harbor and lots of photos as well as briefs on all the courses that I will offer.
Accredited First Aid and CPR Courses. Lifeguard and Community Safety Programs Programs

```html
<!DOCTYPE html>
<html lang="en">
<head>
<meta charset="utf-8">
<title>Harborline Safety Courses — Home</title>
<link href="https://fonts.googleapis.com/css2?family=Lato:wght@400;700;900&family=Arimo:wght@400;700&display=swap" rel="stylesheet">
<style>
  :root {
    --orange: #f07b1c;
    --blue: #2f8fd3;
    --blue-band: rgba(47, 143, 211, 0.88);
    --ink: #222222;
    --text: #333333;
    --light: #f2f2f2;
    --footer: #262626;
    --white: #ffffff;
  }
  * { box-sizing: border-box; margin: 0; padding: 0; }
  html, body { width: 1200px; height: 2490px; overflow: hidden; }
  body { position: relative; font-family: "Lato", sans-serif; color: var(--text); background: var(--white); }

  /* Hero */
  .hero { position: absolute; left: 0; top: 0; width: 1200px; height: 906px;
    background: linear-gradient(180deg, #3f5fb8 0%, #5a7fd0 28%, #2f4f3a 36%, #3e6a44 42%, #d9b98e 55%, #e6c9a0 100%); }
  .brand { position: absolute; left: 78px; top: 60px; width: 240px; display: flex; align-items: center; gap: 14px; }
  .brand-dot { width: 64px; height: 64px; border-radius: 50%; border: 4px solid var(--white); flex: none; }
  .brand-name { font-family: "Lato", sans-serif; font-weight: 900; font-size: 24px; line-height: 1.15; color: var(--white); }
  .main-nav { position: absolute; top: 88px; right: 38px; display: flex; align-items: center; gap: 4px; }
  .main-nav a { font-family: "Lato", sans-serif; font-size: 19px; color: var(--white); text-decoration: none;
    padding: 9px 22px; border-radius: 24px; letter-spacing: 0.3px; }
  .main-nav a.active { background: var(--orange); }
  .tagline { position: absolute; left: 0; top: 420px; width: 1200px; text-align: center; }
  .tagline span { display: inline-block; background: var(--blue-band); color: var(--white);
    font-family: "Lato", sans-serif; font-weight: 900; font-size: 52px; line-height: 70px; padding: 0 36px; }

  /* About */
  .section-title { font-family: "Lato", sans-serif; font-weight: 900; color: var(--ink); text-align: center; }
  .rule { width: 76px; height: 4px; background: var(--blue); margin: 0 auto; }
  .about-title { position: absolute; top: 955px; left: 0; width: 1200px; font-size: 54px; }
  .about-rule { position: absolute; top: 1024px; left: 562px; }
  .about-copy { position: absolute; top: 1062px; left: 80px; width: 1040px; text-align: center;
    font-size: 16.5px; line-height: 31.5px; color: #333; }
  .wave { position: absolute; left: 0; top: 1195px; width: 1200px; height: 205px;
    background: linear-gradient(180deg, #ffffff 0%, #bfe8ef 18%, #2fb4c8 45%, #1a8fa6 75%, #18778f 100%); }
  .btn { position: absolute; display: block; width: 206px; height: 60px; border-radius: 30px; background: var(--orange);
    color: var(--white); font-family: "Lato", sans-serif; font-weight: 900; font-size: 20px; line-height: 60px;
    text-align: center; text-decoration: none; left: 497px; }
  .btn-read { top: 1260px; }

  /* Courses */
  .courses { position: absolute; left: 0; top: 1400px; width: 1200px; height: 637px; background: var(--light); }
  .courses-title { position: absolute; top: 1448px; left: 0; width: 1200px; font-family: "Arimo", sans-serif;
    font-weight: 700; font-size: 50px; letter-spacing: 1.5px; }
  .courses-rule { position: absolute; top: 1518px; left: 562px; }
  .course-card { position: absolute; top: 1566px; width: 328px; text-align: center; }
  .course-photo { width: 328px; height: 252px; }
  .course-name { margin-top: 18px; font-family: "Arimo", sans-serif; font-weight: 700; font-size: 19px;
    line-height: 30px; color: var(--ink); letter-spacing: 0.3px; }
  .course-price { margin-top: 10px; font-family: "Arimo", sans-serif; font-weight: 700; font-size: 18px; color: var(--orange); }
  .slider-arrow { position: absolute; top: 1737px; width: 20px; height: 30px; }
  .btn-all { top: 2007px; z-index: 2; }

  /* Footer */
  .site-footer { position: absolute; left: 0; top: 2037px; width: 1200px; height: 453px; background: var(--footer); color: var(--white); }
  .footer-brand { position: absolute; left: 78px; top: 170px; width: 240px; display: flex; align-items: center; gap: 14px; }
  .footer-brand .brand-dot { border-color: var(--blue); }
  .footer-brand .brand-name { color: var(--orange); }
  .footer-col { position: absolute; top: 107px; }
  .footer-col h4 { font-family: "Lato", sans-serif; font-weight: 700; font-size: 19px; color: var(--blue); letter-spacing: 0.3px; }
  .sitemap { left: 368px; }
  .sitemap a { display: block; color: var(--white); text-decoration: none; font-size: 16px; margin-top: 18px; line-height: 20px; }
  .sitemap h4 + a { margin-top: 16px; }
  .contact { left: 571px; }
  .contact p { font-size: 16px; line-height: 20px; margin-top: 12px; letter-spacing: 0.3px; }
  .contact .contact-name { color: var(--orange); font-size: 17px; margin-top: 16px; }
  .follow { left: 906px; }
  .social { display: flex; gap: 20px; margin-top: 18px; }
  .social span { width: 24px; height: 24px; border-radius: 50%; background: var(--white); display: block; }
  .copyright { position: absolute; left: 0; top: 398px; width: 1200px; text-align: center; font-size: 14.5px; color: #e6e6e6; }
</style>
</head>
<body>

<header class="hero" role="img" aria-label="Photo of lifeguard trainees in blue uniforms on a beach around a rescue trailer and buggy, pine trees behind">
  <div class="brand"><span class="brand-dot"></span><span class="brand-name">Harborline Safety Courses</span></div>
  <nav class="main-nav">
    <a class="active" href="#">HOME</a>
    <a href="#">ABOUT</a>
    <a href="#">COURSES</a>
    <a href="#">GALLERY</a>
    <a href="#">CONTACT</a>
  </nav>
  <h1 class="tagline"><span>Accredited training from first</span><br><span>aid to lifeguard programs</span></h1>
</header>

<h2 class="section-title about-title">About Us</h2>
<div class="rule about-rule"></div>
<p class="about-copy">Harborline Safety Courses delivers a series of Emergency training accreditation and innovative general safety awareness programs. From general first aid to Lifeguard training courses, our carefully designed training methods ensure all students leave with clarity and confidence in managing emergency scenarios. We ensure our training programs are facilitated in a way that enhances learning through shared practical knowledge and shared relatable experiences.</p>
<div class="wave" role="img" aria-label="Photo of a breaking turquoise ocean wave"></div>
<a class="btn btn-read" href="#">Read More</a>

<section class="courses"></section>
<h2 class="section-title courses-title">Upcoming Courses</h2>
<div class="rule courses-rule"></div>

<svg class="slider-arrow" style="left:43px" viewBox="0 0 20 30"><polyline points="15,3 4,15 15,27" fill="none" stroke="#333" stroke-width="2"/></svg>
<svg class="slider-arrow" style="left:1137px" viewBox="0 0 20 30"><polyline points="5,3 16,15 5,27" fill="none" stroke="#333" stroke-width="2"/></svg>

<article class="course-card" style="left:75px">
  <div class="course-photo" role="img" aria-label="Photo of trainees practising CPR on a sandy beach" style="background:linear-gradient(180deg,#8fb3d9 0%,#c9b58f 25%,#d8c39e 70%,#c7503a 100%)"></div>
  <h3 class="course-name">Provide Cardiopulmonary<br>Resuscitation Hltaid009</h3>
  <p class="course-price">$60.00</p>
</article>
<article class="course-card" style="left:437px">
  <div class="course-photo" role="img" aria-label="Photo of students practising CPR on manikins by a pool deck" style="background:linear-gradient(160deg,#9fd8ee 0%,#e9e4dc 35%,#a0784e 75%,#6b4a2e 100%)"></div>
  <h3 class="course-name">Provide Cardiopulmonary<br>Resuscitation Hltaid009</h3>
  <p class="course-price">$60.00</p>
</article>
<article class="course-card" style="left:798px">
  <div class="course-photo" role="img" aria-label="Photo of a team lifting a spinal board in an empty blue pool" style="background:linear-gradient(180deg,#7a7f86 0%,#2b7fd6 15%,#1e6cc8 70%,#2a74cf 100%)"></div>
  <h3 class="course-name">Provide Cardiopulmonary<br>Resuscitation Hltaid009</h3>
  <p class="course-price">$60.00</p>
</article>

<a class="btn btn-all" href="#">View All Courses</a>

<footer class="site-footer">
  <div class="footer-brand"><span class="brand-dot"></span><span class="brand-name">Harborline Safety Courses</span></div>
  <div class="footer-col sitemap">
    <h4>SITE MAP</h4>
    <a href="#">Home</a>
    <a href="#">About</a>
    <a href="#">Courses</a>
    <a href="#">Gallery</a>
    <a href="#">Contact</a>
  </div>
  <div class="footer-col contact">
    <h4>CONTACT DETAILS</h4>
    <p class="contact-name">Daniel Reyes</p>
    <p>0412 555 018</p>
    <p>daniel@harborlinesafetycourses.example.au</p>
  </div>
  <div class="footer-col follow">
    <h4>FOLLOW US</h4>
    <div class="social"><span></span><span></span><span></span><span></span><span></span></div>
  </div>
  <p class="copyright">© Copyright 2021 Harborline Safety Courses. All Right Reserved</p>
</footer>

</body>
</html>
```